Banner ad design for Vantor Reach Ads

We are looking for a designer to develop a concept for banner ads for a Vantor Reach campaign we are building.

We have 3 business lines, shredding services, records management services and scanning services.

We are looking for 4 sets of ads to be created, one for each business line + one set that showcases all of our lines together.

For the design concepts, we would like to see a few sizes (banner, square, leaderboard, skyscraper, etc) for each.

The person chosen will then need to create the ads into all Vantor supported sizes -- 20 sizes total for each set of ads as per the Vantor size guidelines found on this page - https://help.vantor.example/vantor-ads/answer/4859210?hl=en&ref_topic=6082714#

A few items to note:
- Design should complement our existing brand/website look and feel (www.gold-kettle.ca)
- Each final ad must be 150Kb or less in size
- Final designs should be editable, meaning if we would like to change some copy in the design, we can do so using a well-known software (Canva, Photoshop/InDesign, etc)
- Some images are attached for use, but if you feel a different stock image is more suitable to to your design, please go ahead and use it.

Provided below is some messaging that can be used for each set of ads. Do not feel you need to use all of the messaging, it is provided for guidance.

SHREDDING SERVICES:

Possible Short Headline:
-- One-Time Shredding Services
-- Secure Shredding Services
-- Affordable On-Site Shredding

Possible Long Headline
-- Your Paper Can be Destroyed as Soon as the Next Business Day

Possible Descriptions:
-- QVRB AAA Certified On site shredding company. Service as soon as Next Day.
-- Secure and Affordable Toronto & GTA On-Site Shredding.
-- Certified, Affordable Office Shredding Since 2003.
-- Quick, no contact and affordable paper shredding services in Toronto & Southern Ontario.
-- Certified, Affordable Office Shredding Since 2003. Fast, no contact shredding service.

Call to Action
-- Get a Quote

RECORDS MANAGEMENT
Short Headline:
-- Off-site Records Storage
-- Records Management & Storage
-- Secure Records Storage
-- Records Management Services
-- Long Term Records Management
-- Document Storage Solutions

Possible Description
-- Local, Affordable Storage Solutions. Protect and Store your Documents in our Secure Facility
-- Local, Affordable Records Management Solutions. Store your Records in our Secure Facility
-- Certified, Affordable Document Storage Since 2004. Contact Us for a Free Quote!
-- Vaultmark+ Certified, Affordable Document Storage Since 2004. Contact Us for a Free Quote!

Call to Action
-- Get a Quote

SCANNING SERVICES

Short Headline:
-- Professional Scanning Company
-- Toronto & GTA Scanning Service
-- Document Scanning Services
-- Digital Conversion Services
-- Fast & Easy Retrieval

Description
-- Scan and documents and files with Professional scanning services from Gold-Kettle
-- Convert Your Paper Files to Electronic Files. Fast & Easy Retrieval.
-- Easily access your documents electronically with Document Scanning Services

Call to Action
-- Get a Quote

ALL SERVICES AD SET
Short Headline
-- Shred, Scan & Store Documents
-- Secure Shredding, Records Management and Scanning Services
-- #1 Document Management Company
-- Gold Kettle Shredding, Storage & Scanning

Description
-- Secure and Affordable Toronto & GTA On-Site Shredding, Document Storage & Scanning Company

Call to Action
-- Get a Quote

Font styles to use
Sans Serif

```html
<!DOCTYPE html>
<html lang="en">
<head>
<meta charset="utf-8">
<title>Document Storage Solutions – Banner Set</title>
<link rel="stylesheet" href="https://fonts.googleapis.com/css2?family=Montserrat:wght@500;600;800&display=swap">
<style>
  :root {
    --board: #e4e4e4;
    --white: #ffffff;
    --blue-deep: #2a6db5;
    --blue-light: #4aa6e6;
    --green: #1dbf57;
    --ink: #1d2b3a;
    --logo-blue: #1f8fd6;
  }
  * { box-sizing: border-box; margin: 0; padding: 0; }
  html, body { width: 1200px; height: 1188px; overflow: hidden; }
  body {
    position: relative;
    background: var(--board);
    font-family: "Montserrat", Arial, sans-serif;
  }
  .ad {
    position: absolute;
    overflow: hidden;
    background: var(--white);
  }
  .ad svg.shapes, .ad svg.photo {
    position: absolute; inset: 0; width: 100%; height: 100%;
  }
  .headline {
    position: absolute;
    color: var(--white);
    font-weight: 800;
    line-height: 1.28;
    white-space: nowrap;
  }
  .description {
    position: absolute;
    color: var(--white);
    font-weight: 500;
    white-space: nowrap;
  }
  .cta {
    position: absolute;
    display: flex; align-items: center; justify-content: center;
    background: var(--green);
    color: var(--white);
    font-weight: 600;
    border-radius: 3px;
  }
  .brand {
    position: absolute;
    display: flex; align-items: center; gap: 6px;
    color: var(--ink);
    font-weight: 600;
  }
  .brand-mark { background: var(--logo-blue); }

  /* Leaderboard */
  .ad-leaderboard { left: 6px; top: 3px; width: 1191px; height: 148px; }
  .ad-leaderboard .headline { right: 24px; top: 16px; font-size: 36px; text-align: right; }
  .ad-leaderboard .description { right: 24px; top: 72px; font-size: 16.5px; line-height: 1.5; text-align: right; }
  .ad-leaderboard .cta { left: 468px; top: 75px; width: 256px; height: 57px; font-size: 20px; }
  .ad-leaderboard .brand { left: 12px; top: 112px; font-size: 14px; }
  .ad-leaderboard .brand-mark { width: 9px; height: 9px; }

  /* Medium rectangle */
  .ad-rectangle { left: 3px; top: 201px; width: 493px; height: 410px; }
  .ad-rectangle .headline { left: 32px; top: 22px; font-size: 32px; line-height: 42px; }
  .ad-rectangle .description { left: 32px; top: 160px; font-size: 14px; line-height: 23px; }
  .ad-rectangle .cta { left: 262px; top: 340px; width: 205px; height: 57px; font-size: 17px; }
  .ad-rectangle .brand { left: 24px; top: 352px; font-size: 19px; }
  .ad-rectangle .brand-mark { width: 11px; height: 11px; }

  /* Square */
  .ad-square { left: 3px; top: 726px; width: 551px; height: 459px; }
  .ad-square .headline { left: 32px; top: 24px; font-size: 32px; line-height: 42px; }
  .ad-square .description { left: 32px; top: 172px; font-size: 15px; line-height: 23px; }
  .ad-square .cta { left: 277px; top: 380px; width: 230px; height: 64px; font-size: 19px; }
  .ad-square .brand { left: 30px; top: 400px; font-size: 21px; }
  .ad-square .brand-mark { width: 12px; height: 12px; }

  /* Half page */
  .ad-halfpage { left: 701px; top: 201px; width: 496px; height: 984px; }
  .ad-halfpage .headline { left: 0; right: 0; top: 46px; font-size: 38px; line-height: 49px; text-align: center; }
  .ad-halfpage .description { left: 0; right: 0; top: 160px; font-size: 19.5px; line-height: 33px; text-align: center; }
  .ad-halfpage .cta { left: 228px; top: 888px; width: 230px; height: 64px; font-size: 19px; }
  .ad-halfpage .brand { left: 26px; top: 906px; font-size: 21px; }
  .ad-halfpage .brand-mark { width: 12px; height: 12px; }
</style>
</head>
<body>
<svg width="0" height="0" style="position:absolute">
  <defs>
    <linearGradient id="panel-blue" x1="0" y1="0" x2="0.4" y2="1">
      <stop offset="0" stop-color="#2a6db5"/>
      <stop offset="1" stop-color="#4aa6e6"/>
    </linearGradient>
    <linearGradient id="shelving" x1="0" y1="0" x2="1" y2="1">
      <stop offset="0" stop-color="#5a5048"/>
      <stop offset="0.5" stop-color="#b9a588"/>
      <stop offset="1" stop-color="#d9ccb6"/>
    </linearGradient>
  </defs>
</svg>

<section class="ad ad-leaderboard">
  <svg class="photo" viewBox="0 0 1191 148" preserveAspectRatio="none" role="img" aria-label="Warehouse aisle with tall blue racking stacked with archive boxes">
    <polygon points="0,0 480,0 635,148 170,148 0,55" fill="url(#shelving)"/>
  </svg>
  <svg class="shapes" viewBox="0 0 1191 148" preserveAspectRatio="none" aria-hidden="true">
    <polygon points="492,0 1191,0 1191,148 647,148" fill="url(#panel-blue)"/>
  </svg>
  <h2 class="headline">Document Storage Solutions</h2>
  <p class="description">Local, Affordable Storage Solutions. Protect and<br>Store your Documents in our Secure Facility</p>
  <a class="cta">Get a Quote</a>
  <div class="brand"><span class="brand-mark"></span>gold-kettle</div>
</section>

<section class="ad ad-rectangle">
  <svg class="photo" viewBox="0 0 493 410" preserveAspectRatio="none" role="img" aria-label="Warehouse racking loaded with archive boxes">
    <polygon points="397,0 493,0 493,338 202,308" fill="url(#shelving)"/>
  </svg>
  <svg class="shapes" viewBox="0 0 493 410" preserveAspectRatio="none" aria-hidden="true">
    <polygon points="0,0 385,0 190,307 0,288" fill="url(#panel-blue)"/>
  </svg>
  <h2 class="headline">Document<br>Storage<br>Solutions</h2>
  <p class="description">Local, Affordable Storage<br>Solutions. Protect and<br>Store your Documents in<br>our Secure Facility</p>
  <div class="brand"><span class="brand-mark"></span>gold-kettle</div>
  <a class="cta">Get a Quote</a>
</section>

<section class="ad ad-square">
  <svg class="photo" viewBox="0 0 551 459" preserveAspectRatio="none" role="img" aria-label="Warehouse racking loaded with archive boxes">
    <polygon points="397,0 551,0 551,382 192,342" fill="url(#shelving)"/>
  </svg>
  <svg class="shapes" viewBox="0 0 551 459" preserveAspectRatio="none" aria-hidden="true">
    <polygon points="0,0 383,0 180,340 0,318" fill="url(#panel-blue)"/>
  </svg>
  <h2 class="headline">Document<br>Storage<br>Solutions</h2>
  <p class="description">Local, Affordable Storage<br>Solutions. Protect and<br>Store your Documents in<br>our Secure Facility</p>
  <div class="brand"><span class="brand-mark"></span>gold-kettle</div>
  <a class="cta">Get a Quote</a>
</section>

<section class="ad ad-halfpage">
  <svg class="photo" viewBox="0 0 496 984" preserveAspectRatio="none" role="img" aria-label="Tall warehouse racking stacked with archive boxes">
    <polygon points="0,381 496,349 496,790 0,800" fill="url(#shelving)"/>
  </svg>
  <svg class="shapes" viewBox="0 0 496 984" preserveAspectRatio="none" aria-hidden="true">
    <polygon points="0,0 496,0 496,340 0,289" fill="url(#panel-blue)"/>
    <polygon points="270,832 496,790 496,868" fill="url(#panel-blue)"/>
  </svg>
  <h2 class="headline">Document Storage<br>Solutions</h2>
  <p class="description">Local, Affordable Storage<br>Solutions. Protect and Store your<br>Documents in our Secure Facility</p>
  <div class="brand"><span class="brand-mark"></span>gold-kettle</div>
  <a class="cta">Get a Quote</a>
</section>
</body>
</html>
```